brisk-vale.com Real Estate, Investment, Financial corporate

Real Estate, Investment, Financial corporate looking site. Show present a professional firm, with an elegant display. Please see the attached file which includes the logo, palette and fonts.
Updates

We just starting the brief today. ( logo was delayed)

Target Market(s)

Investors, Corporate , B2b

Industry/Entity Type

real-estate investments

Number of Pages Required

3 page

Requirements
Must have
• Dazzling Homepage
Nice to have
• paralex

```html
<!DOCTYPE html>
<html lang="en">
<head>
<meta charset="utf-8">
<title>Services — Brisk Vale</title>
<link href="https://fonts.googleapis.com/css2?family=Nunito+Sans:wght@300;400;600&family=Nunito:wght@400;600&display=swap" rel="stylesheet">
<style>
:root{
  --gold:#f2c98c;
  --gold-soft:#f5d2a1;
  --ink:#1c1c1c;
  --text:#666666;
  --black:#000000;
  --white:#ffffff;
  --footer-bg:#f9f9f9;
}
*{margin:0;padding:0;box-sizing:border-box}
html,body{width:1200px;height:2498px;overflow:hidden;background:var(--white)}
body{position:relative;font-family:"Nunito Sans",sans-serif;color:var(--text)}
.abs{position:absolute}

/* Hero */
.hero{left:0;top:0;width:1200px;height:536px;
  clip-path:polygon(0 0,100% 0,100% 496px,50% 536px,0 496px);
  background:
    radial-gradient(ellipse at 30% 45%,rgba(232,176,98,.85) 0%,rgba(150,100,55,.6) 35%,rgba(60,40,30,0) 65%),
    linear-gradient(100deg,#5a4535 0%,#8a6a48 30%,#2f3ccf 62%,#2a35d6 80%,#1d2a9a 100%);}
.hero-ground{left:0;top:0;width:1200px;height:536px;
  clip-path:polygon(0 0,100% 0,100% 496px,50% 536px,0 496px);
  background:linear-gradient(180deg,rgba(0,0,0,0) 55%,rgba(40,30,40,.55) 78%,rgba(70,200,190,.35) 92%,rgba(30,20,30,.6) 100%)}
.brand{left:118px;top:26px;display:flex;align-items:center;gap:12px}
.brand-mark{width:46px;height:46px;border:2px solid var(--gold-soft)}
.brand-name{font-family:"Nunito",sans-serif;font-size:28px;color:var(--gold-soft);font-weight:400}
.nav{top:42px;left:877px;display:flex;gap:32px;font-size:11px}
.nav a{color:var(--ink);text-decoration:none}
.crumbs{left:0;width:1200px;top:208px;text-align:center;font-size:9px;letter-spacing:1px;color:rgba(40,30,30,.55);text-transform:uppercase}
.hero-title{left:0;width:1200px;top:232px;text-align:center;font-size:48px;font-weight:300;color:#111}

/* Section labels */
.eyebrow{display:flex;align-items:center;justify-content:center;gap:8px;font-size:9px;letter-spacing:1.4px;text-transform:uppercase;font-weight:600}
.eyebrow::before,.eyebrow::after{content:"";width:38px;height:1px;background:var(--gold)}
.services-label{left:0;width:1200px;top:627px;color:var(--gold)}
.services-title{left:0;width:1200px;top:648px;text-align:center;font-size:30px;font-weight:400;color:var(--ink)}

.feature{width:214px;text-align:center}
.feature svg{display:block;margin:0 auto}
.feature h3{font-size:18px;font-weight:400;color:var(--ink);margin-top:22px}
.feature p{font-size:12px;line-height:22.5px;margin-top:10px}

/* How it works */
.flow-panel{left:38px;top:1010px;width:562px;height:752px;background:var(--black);
  clip-path:polygon(0 0,100% 0,100% 100%,0 714px)}
.flow-photo{left:600px;top:1010px;width:562px;height:752px;
  clip-path:polygon(0 0,100% 0,100% 714px,0 100%);
  background:
    radial-gradient(ellipse at 20% 30%,rgba(250,215,150,.55) 0%,rgba(0,0,0,0) 30%),
    linear-gradient(180deg,#e6e2de 0%,#cfc9c2 25%,#b6aea5 48%,#6d5c52 62%,#3b2c25 82%,#2a1e19 100%)}
.flow-label{left:38px;width:562px;top:1091px;color:var(--white)}
.flow-title{left:38px;width:562px;top:1111px;text-align:center;font-size:30px;font-weight:400;color:var(--white)}
.step{width:214px;text-align:center;color:var(--white)}
.step-num{width:70px;height:70px;border-radius:50%;background:var(--gold);margin:0 auto;display:flex;align-items:center;justify-content:center;font-size:24px;font-weight:300;color:var(--white)}
.step h3{font-size:18px;font-weight:400;margin-top:16px;color:var(--white)}
.step p{font-size:12px;line-height:22.5px;margin-top:8px;color:var(--white)}

/* Intro text */
.intro{left:449px;top:1849px;width:634px;font-size:12px;line-height:22.5px}

/* Footer */
.footer{left:0;top:2027px;width:1200px;height:471px;background:var(--footer-bg)}
.footer-col{top:2115px}
.footer-col h4{font-size:15px;font-weight:400;color:var(--ink)}
.footer-col p{font-size:12px;line-height:22.5px;margin-top:34px}
.links{list-style:none;margin-top:34px;font-size:12px;line-height:22.5px;color:#555}
.links li{display:flex;align-items:center;gap:7px}
.links li::before{content:"";width:11px;height:1px;background:var(--gold)}
.social{top:2284px;left:133px;display:flex;gap:34px}
.social span{width:16px;height:16px;border-radius:50%;background:var(--gold-soft)}
.contact{list-style:none;margin-top:34px;font-size:12px;line-height:19px;color:#555}
.contact li{display:flex;gap:20px;margin-bottom:22px}
.contact li span{width:140px}
.contact svg{flex:none;margin-top:3px}
.contact .accent{color:var(--gold-soft)}
.copyright{left:0;width:1200px;top:2380px;text-align:center;font-size:12px;color:#555}
</style>
</head>
<body>

<header>
  <div class="abs hero" role="img" aria-label="Modern hillside villa at dusk with glowing windows and a pool"></div>
  <div class="abs hero-ground"></div>
  <div class="abs brand"><span class="brand-mark"></span><span class="brand-name">Brisk Vale</span></div>
  <nav class="abs nav"><a href="#">Home</a><a href="#">Services</a><a href="#">Contact</a></nav>
  <div class="abs crumbs">Home / Services</div>
  <h1 class="abs hero-title">Services</h1>
</header>

<section>
  <div class="abs eyebrow services-label">Our Services</div>
  <h2 class="abs services-title">The smartest way to buy a home</h2>

  <div class="abs feature" style="left:126px;top:738px">
    <svg width="50" height="50" viewBox="0 0 50 50" fill="none" stroke="#f2c98c" stroke-width="1.5">
      <ellipse cx="26" cy="30" rx="18" ry="13"/><circle cx="22" cy="11" r="7"/><path d="M8 28 H4 M14 40 V46 M34 40 V46 M44 28 l4 -3"/>
    </svg>
    <h3>No Downpayment</h3>
    <p>A small river named Duden flows by their place and supplies it with the necessary regelialia.</p>
  </div>
  <div class="abs feature" style="left:371px;top:738px">
    <svg width="50" height="50" viewBox="0 0 50 50" fill="none" stroke="#f2c98c" stroke-width="1.5">
      <rect x="4" y="12" width="42" height="32" rx="3"/><path d="M8 12 L36 4 L40 12"/><rect x="32" y="23" width="14" height="10"/><circle cx="38" cy="28" r="2"/>
    </svg>
    <h3>All Cash Offer</h3>
    <p>A small river named Duden flows by their place and supplies it with the necessary regelialia.</p>
  </div>
</section>

<section>
  <div class="abs flow-panel"></div>
  <div class="abs flow-photo" role="img" aria-label="Bright living room with sofa, stone fireplace and city view windows"></div>
  <div class="abs eyebrow flow-label">Work Flow</div>
  <h2 class="abs flow-title">How it works</h2>

  <div class="abs step" style="left:126px;top:1223px"><div class="step-num">01</div><h3>Evaluate Property</h3><p>A small river named Duden flows by their place and supplies it with the necessary regelialia.</p></div>
  <div class="abs step" style="left:371px;top:1223px"><div class="step-num">02</div><h3>Meet Your Agent</h3><p>A small river named Duden flows by their place and supplies it with the necessary regelialia.</p></div>
  <div class="abs step" style="left:126px;top:1445px"><div class="step-num">03</div><h3>Close the Deal</h3><p>A small river named Duden flows by their place and supplies it with the necessary regelialia.</p></div>
  <div class="abs step" style="left:371px;top:1445px"><div class="step-num">04</div><h3>Have Your Property</h3><p>A small river named Duden flows by their place and supplies it with the necessary regelialia.</p></div>
</section>

<p class="abs intro">Far far away, behind the word mountains, far from the countries Vokalia and Consonantia, there live the blind texts. Separated they live in Bookmarksgrove right at the coast of the Semantics, a large language ocean. A small river named Duden flows by their place and supplies it with the necessary regelialia. It is a paradisematic country, in which roasted parts of sentences fly into your mouth.</p>

<footer>
  <div class="abs footer"></div>
  <div class="abs footer-col" style="left:123px;width:180px">
    <h4>Uptown</h4>
    <p>Far far away, behind the word mountains, far from the countries.</p>
  </div>
  <div class="abs social"><span></span><span></span></div>
  <div class="abs footer-col" style="left:338px">
    <h4>Community</h4>
    <ul class="links"><li>Search Properties</li><li>For Agents</li><li>Reviews</li><li>FAQs</li></ul>
  </div>
  <div class="abs footer-col" style="left:533px">
    <h4>About Us</h4>
    <ul class="links"><li>Our Story</li><li>Meet the team</li><li>Careers</li></ul>
  </div>
  <div class="abs footer-col" style="left:709px">
    <h4>Company</h4>
    <ul class="links"><li>About Us</li><li>Press</li><li>Contact</li><li>Careers</li></ul>
  </div>
  <div class="abs footer-col" style="left:905px;width:200px">
    <h4>Have a Questions?</h4>
    <ul class="contact">
      <li><svg width="10" height="13" viewBox="0 0 10 13"><path d="M5 0a5 5 0 0 1 5 5c0 3-5 8-5 8S0 8 0 5a5 5 0 0 1 5-5z" fill="#f5d2a1"/><circle cx="5" cy="5" r="1.8" fill="#f9f9f9"/></svg><span>418 Harbor Lane, Suite 12, Portland, Oregon, USA</span></li>
      <li><svg width="12" height="12" viewBox="0 0 12 12"><path d="M2 0l3 3-1.5 1.5a7 7 0 0 0 4 4L9 7l3 3-2 2C5 12 0 7 0 2z" fill="#f5d2a1"/></svg><span class="accent">+1 503 555 0142</span></li>
      <li><svg width="14" height="10" viewBox="0 0 14 10"><rect width="14" height="10" fill="#f5d2a1"/><path d="M0 0l7 5 7-5" stroke="#f9f9f9" fill="none"/></svg><span class="accent">hello@brisk-vale.com</span></li>
    </ul>
  </div>
  <p class="abs copyright">Copyright © 2021 All rights reserved | brisk-vale.com</p>
</footer>

</body>
</html>
```